Quorvantelline.com

I need a site that I can sell dewatering equipment to the construction industry.
Ie, pipes fittings pumps and other such things needed to remove the groundwater on construction sites. Here in Florida, it’s needed almost everywhere seeing we are at sea level.
I want to be able to sell these products on the site and receive

Coded - Design and coding required

1 page

```html
<!DOCTYPE html>
<html lang="en">
<head>
<meta charset="utf-8">
<title>Quorvantelline.com – Groundwater Equipment Store</title>
<link rel="stylesheet" href="https://fonts.googleapis.com/css2?family=Michroma&family=Montserrat:wght@500;600;700&family=Open+Sans:ital,wght@0,400;0,600;0,700;1,600;1,700&display=swap">
<style>
:root{
  --teal:#1c7486;
  --teal-dark:#135a69;
  --teal-light:#2596ad;
  --ink:#333;
  --muted:#555;
  --page:#fff;
  --frame:#e6e6e6;
  --card:#f3f3f3;
}
*{box-sizing:border-box;margin:0;padding:0}
html,body{width:1200px;height:2727px;overflow:hidden}
body{background:var(--frame);font-family:"Open Sans",sans-serif;color:var(--ink)}
.page{position:absolute;left:14px;top:9px;width:1172px;height:2700px;background:var(--page)}
section,footer{position:absolute;left:0;width:1172px}
.abs{position:absolute}

/* hero */
.hero{top:0;height:558px;overflow:hidden}
.hero-photo{position:absolute;inset:0;background:radial-gradient(ellipse at 70% 45%,#3fb3c2 0%,#1c7d8d 35%,#0d4551 70%,#062a33 100%)}
.logo{left:30px;top:30px;font-family:"Montserrat",sans-serif;font-weight:600;font-size:25px;color:#fff;letter-spacing:.3px}
.phone-pill{left:601px;top:27px;width:163px;height:27px;border-radius:14px;background:#1e5c6b;color:#fff;font:600 13px "Montserrat",sans-serif;display:flex;align-items:center;justify-content:center;gap:8px}
.util{top:31px;display:flex;gap:24px;left:802px;color:#fff;font:600 12.5px "Montserrat",sans-serif}
.util span{display:flex;align-items:center;gap:5px}
.nav{top:88px;left:495px;display:flex;align-items:center;gap:22px;color:#fff;font:700 13px "Montserrat",sans-serif}
.nav span{display:flex;align-items:center;gap:6px}
.nav .home{width:36px;height:27px;background:var(--teal);display:flex;align-items:center;justify-content:center}
.hero h1{position:absolute;top:330px;width:100%;text-align:center;color:#fff;font:700 36px "Montserrat",sans-serif;letter-spacing:.3px;text-shadow:0 2px 6px rgba(0,0,0,.5)}
.btn-outline{left:473px;top:384px;width:224px;height:51px;border:2px solid #fff;color:#fff;font:600 17px "Montserrat",sans-serif;letter-spacing:1px;display:flex;align-items:center;justify-content:center}

/* products */
.products{top:558px;height:675px}
.section-title{width:100%;text-align:center;font-family:"Michroma",sans-serif;font-size:20px;color:#333;letter-spacing:1px}
.tabs{top:166px;left:62px;width:1074px;height:43px;border-bottom:2px solid var(--teal)}
.tab{position:absolute;top:0;height:43px;background:var(--teal);color:#fff;font:600 14px "Open Sans",sans-serif;display:flex;align-items:center;justify-content:center}
.tab.active{background:#fff;color:#222;border:2px solid var(--teal);border-bottom:none;height:45px}
.card{position:absolute;top:257px;width:238px}
.card-img{height:194px;background:linear-gradient(180deg,#f7f7f7,#ececec);display:flex;align-items:center;justify-content:center}
.card-img .pump{width:88%;height:75%;border-radius:6px}
.pump.red{background:linear-gradient(180deg,#e23a3a,#b51818)}
.pump.blue{background:linear-gradient(180deg,#3a6fe0,#1a3fa8)}
.card-body{margin-top:6px;height:125px;background:var(--card);padding:18px 18px 0;box-shadow:0 3px 6px rgba(0,0,0,.12)}
.card-body h3{font:600 15px "Open Sans",sans-serif;color:#333}
.card-body p{font:600 14px "Open Sans",sans-serif;color:#333;margin-top:3px}
.price{margin-top:16px;border-top:1px solid #d8d8d8;padding-top:12px;display:flex;align-items:center;justify-content:space-between;font:700 16px "Open Sans",sans-serif}
.price .amt{display:flex;align-items:center;gap:6px}
.coin{width:24px;height:24px;border:2px solid #333;border-radius:50%;font-size:13px;display:flex;align-items:center;justify-content:center}
.arrow{top:416px}

/* testimonials */
.testimonials{top:1233px;height:478px;overflow:hidden}
.testimonials-photo{position:absolute;inset:0;background:linear-gradient(135deg,#3a8a97 0%,#1f6e80 50%,#185f70 100%)}
.testimonials .section-title{position:absolute;top:95px;color:#fff;font-size:21px}
.quote{position:absolute;top:167px;width:324px;height:173px;background:rgba(255,255,255,.82);border-radius:6px;padding:22px 10px 0 58px;font-size:14px;line-height:20.5px;color:#333;white-space:nowrap}
.quote::after{content:"";position:absolute;left:22px;bottom:-16px;border-right:18px solid transparent;border-top:16px solid rgba(255,255,255,.82)}
.qmark{position:absolute;left:16px;top:14px;font:700 44px/1 Georgia,serif;color:#555}
.qclose{display:inline-block;margin-left:8px;font:700 44px/1 Georgia,serif;color:#555;vertical-align:-22px;height:20px}
.avatar{position:absolute;width:92px;height:92px;border-radius:50%;border:4px solid #fff;background:linear-gradient(180deg,#d9e4e8,#a9bcc4)}
.tname{position:absolute;top:360px;color:#fff;font:italic 700 15.5px "Open Sans",sans-serif}

/* about */
.about{top:1711px;height:584px}
.about h2{position:absolute;left:53px;top:96px;font-family:"Michroma",sans-serif;font-size:17px;color:#222;letter-spacing:1px}
.about p{position:absolute;left:53px;top:168px;width:620px;font-size:14px;line-height:20.5px;color:#333}
.btn-solid{left:51px;top:312px;width:220px;height:49px;background:var(--teal);color:#fff;font:600 18px "Montserrat",sans-serif;letter-spacing:1px;display:flex;align-items:center;justify-content:center}
.about-ring{left:722px;top:89px;width:400px;height:400px;border-radius:50%;background:#efefef}
.about-photo{position:absolute;left:27px;top:27px;width:346px;height:346px;border-radius:50%;background:linear-gradient(180deg,#a9c4db 0%,#c9d4dc 45%,#8c7f6c 75%,#6e5f4c 100%)}

/* footer */
.site-footer{top:2295px;height:369px;background:var(--teal);color:#fff}
.footer-logo{top:60px;width:100%;text-align:center;font:600 22px "Montserrat",sans-serif}
.fcol{position:absolute;top:130px}
.fcol h4{font:700 14px "Open Sans",sans-serif;letter-spacing:.5px;padding-bottom:12px;border-bottom:1px solid rgba(255,255,255,.35);margin-bottom:16px}
.fcol li{list-style:none;font:600 12.5px/19px "Open Sans",sans-serif}
.contact-row{display:flex;gap:10px;font:600 12.5px/18px "Open Sans",sans-serif;margin-bottom:18px}
.social{display:flex;align-items:center;gap:14px;font:600 13px "Open Sans",sans-serif;margin-bottom:14px}
.social i{width:20px;height:20px;border-radius:50%;background:#fff;display:block}
.newsletter{display:flex;height:36px}
.newsletter .field{width:166px;background:#fff;color:#333;font:600 12px "Open Sans",sans-serif;display:flex;align-items:center;padding-left:8px;border:2px solid #fff}
.newsletter .go{width:91px;background:var(--teal-light);font:700 13px "Open Sans",sans-serif;display:flex;align-items:center;justify-content:center}
.copyright{position:absolute;top:2664px;left:0;width:1172px;height:36px;display:flex;align-items:center;justify-content:center;font:600 11px "Open Sans",sans-serif;letter-spacing:.5px;color:#333}
</style>
</head>
<body>
<div class="page">

  <section class="hero">
    <div class="hero-photo" role="img" aria-label="Close-up photo of large teal steel pipes with bolted flanges"></div>
    <div class="abs logo">Quorvantelline.com</div>
    <div class="abs phone-pill">
      <svg width="13" height="13" viewBox="0 0 24 24"><path fill="#fff" d="M6.6 10.8a15 15 0 0 0 6.6 6.6l2.2-2.2c.3-.3.7-.4 1-.2 1.1.4 2.3.6 3.6.6.6 0 1 .4 1 1V20c0 .6-.4 1-1 1A17 17 0 0 1 3 4c0-.6.4-1 1-1h3.5c.6 0 1 .4 1 1 0 1.3.2 2.5.6 3.6.1.3 0 .7-.2 1z"/></svg>
      1800.555.0142
    </div>
    <div class="abs util">
      <span><svg width="11" height="11" viewBox="0 0 24 24"><circle cx="12" cy="7" r="5" fill="#fff"/><path fill="#fff" d="M2 23c0-6 4-9 10-9s10 3 10 9z"/></svg>LOGIN</span>
      <span><svg width="12" height="12" viewBox="0 0 24 24"><circle cx="12" cy="12" r="10" fill="none" stroke="#fff" stroke-width="2.5"/><path d="M12 7v10M7 12h10" stroke="#fff" stroke-width="2.5"/></svg>REGISTER</span>
      <span><svg width="13" height="12" viewBox="0 0 24 22"><path d="M1 2h4l3 12h12l3-9H7" fill="none" stroke="#fff" stroke-width="2.5"/><circle cx="10" cy="19" r="2" fill="#fff"/><circle cx="18" cy="19" r="2" fill="#fff"/></svg>CART</span>
      <span><svg width="12" height="12" viewBox="0 0 24 24"><circle cx="10" cy="10" r="7" fill="none" stroke="#fff" stroke-width="3"/><path d="M15 15l7 7" stroke="#fff" stroke-width="3"/></svg>SEARCH</span>
    </div>
    <nav class="abs nav">
      <span class="home"><svg width="16" height="14" viewBox="0 0 24 22"><path fill="#fff" d="M12 1 1 11h3v10h6v-6h4v6h6V11h3z"/></svg></span>
      <span><svg width="14" height="12" viewBox="0 0 24 20"><path d="M3 2v10h18" fill="none" stroke="#fff" stroke-width="3"/></svg>PRODUCTS</span>
      <span><svg width="14" height="12" viewBox="0 0 24 20"><rect x="2" y="2" width="20" height="6" fill="#fff"/><rect x="4" y="10" width="16" height="9" fill="#fff"/></svg>SHOP</span>
      <span><svg width="16" height="13" viewBox="0 0 26 20"><rect x="1" y="1" width="16" height="11" rx="2" fill="none" stroke="#fff" stroke-width="2"/><rect x="8" y="7" width="16" height="11" rx="2" fill="none" stroke="#fff" stroke-width="2"/></svg>TESTIMONIALS</span>
      <span><svg width="14" height="13" viewBox="0 0 24 22"><rect x="2" y="2" width="20" height="13" rx="2" fill="#fff"/><path d="M6 15v6l6-6z" fill="#fff"/></svg>ABOUT</span>
      <span><svg width="15" height="12" viewBox="0 0 24 18"><rect x="1" y="1" width="22" height="16" fill="none" stroke="#fff" stroke-width="2"/><path d="M1 1l11 9 11-9" fill="none" stroke="#fff" stroke-width="2"/></svg>CONTACT</span>
    </nav>
    <h1>THE LEADING SUPPLIER FOR DEWATERING INDUSTRY</h1>
    <div class="abs btn-outline">SHOP NOW</div>
  </section>

  <section class="products">
    <h2 class="section-title abs" style="top:94px">PRODUCTS</h2>
    <div class="abs tabs">
      <div class="tab active" style="left:0;width:168px">Well Point Pumps</div>
      <div class="tab" style="left:177px;width:167px">Jet Pumps</div>
      <div class="tab" style="left:353px;width:167px">Hydraulic Pumps</div>
      <div class="tab" style="left:528px;width:167px">Header Pipe</div>
      <div class="tab" style="left:704px;width:167px">Header Pipe Plug</div>
      <div class="tab" style="left:879px;width:167px">Accessories</div>
    </div>

    <svg class="abs arrow" style="left:46px" width="20" height="30" viewBox="0 0 20 30"><path d="M15 3 4 15l11 12" fill="none" stroke="#555" stroke-width="5"/></svg>
    <svg class="abs arrow" style="left:1106px" width="20" height="30" viewBox="0 0 20 30"><path d="M5 3l11 12L5 27" fill="none" stroke="#555" stroke-width="5"/></svg>

    <div class="card" style="left:93px">
      <div class="card-img"><div class="pump red" role="img" aria-label="Photo of a red well point pump unit"></div></div>
      <div class="card-body"><h3>Well Point Pump</h3><p>AB - 100</p>
        <div class="price"><span class="amt"><span class="coin">$</span>1545.00</span><svg width="22" height="18" viewBox="0 0 24 20"><path d="M1 2h4l3 11h12l3-8H6" fill="#333" stroke="#333" stroke-width="2"/><circle cx="10" cy="17" r="2" fill="#333"/><circle cx="18" cy="17" r="2" fill="#333"/></svg></div></div>
    </div>
    <div class="card" style="left:342px">
      <div class="card-img"><div class="pump blue" role="img" aria-label="Photo of a blue well point pump unit"></div></div>
      <div class="card-body"><h3>Well Point Pump</h3><p>AB - 101</p>
        <div class="price"><span class="amt"><span class="coin">$</span>2485.00</span><svg width="22" height="18" viewBox="0 0 24 20"><path d="M1 2h4l3 11h12l3-8H6" fill="#333" stroke="#333" stroke-width="2"/><circle cx="10" cy="17" r="2" fill="#333"/><circle cx="18" cy="17" r="2" fill="#333"/></svg></div></div>
    </div>
    <div class="card" style="left:591px">
      <div class="card-img"><div class="pump red" role="img" aria-label="Photo of a red well point pump unit"></div></div>
      <div class="card-body"><h3>Well Point Pump</h3><p>AB - 102</p>
        <div class="price"><span class="amt"><span class="coin">$</span>1585.00</span><svg width="22" height="18" viewBox="0 0 24 20"><path d="M1 2h4l3 11h12l3-8H6" fill="#333" stroke="#333" stroke-width="2"/><circle cx="10" cy="17" r="2" fill="#333"/><circle cx="18" cy="17" r="2" fill="#333"/></svg></div></div>
    </div>
    <div class="card" style="left:841px">
      <div class="card-img"><div class="pump blue" role="img" aria-label="Photo of a blue well point pump unit"></div></div>
      <div class="card-body"><h3>Well Point Pump</h3><p>AB - 103</p>
        <div class="price"><span class="amt"><span class="coin">$</span>3745.00</span><svg width="22" height="18" viewBox="0 0 24 20"><path d="M1 2h4l3 11h12l3-8H6" fill="#333" stroke="#333" stroke-width="2"/><circle cx="10" cy="17" r="2" fill="#333"/><circle cx="18" cy="17" r="2" fill="#333"/></svg></div></div>
    </div>
  </section>

  <section class="testimonials">
    <div class="testimonials-photo" role="img" aria-label="Teal-tinted photo of workers installing dewatering pipe on a construction site"></div>
    <h2 class="section-title">TESTIMONIALS</h2>

    <div class="quote" style="left:73px"><span class="qmark">“</span>Lorem ipsum dolor sit amet, consect<br>er adipiscing elit, sed diam nonummy<br>nibh euismod tincidunt ut laoreet do<br>magna aliquam erat volu. Wisi enim<br>minim veniam.<span class="qclose">”</span></div>
    <div class="avatar" style="left:285px;top:299px" role="img" aria-label="Portrait of customer Marisa Delacourt"></div>
    <div class="tname" style="left:76px">Marisa Delacourt</div>

    <div class="quote" style="left:424px"><span class="qmark">“</span>Lorem ipsum dolor sit amet, consect<br>er adipiscing elit, sed diam nonummy<br>nibh euismod tincidunt ut laoreet do<br>magna aliquam erat volu. Wisi enim<br>minim veniam.<span class="qclose">”</span></div>
    <div class="avatar" style="left:636px;top:299px" role="img" aria-label="Portrait of customer Nadia Brenholt"></div>
    <div class="tname" style="left:427px">Nadia Brenholt</div>

    <div class="quote" style="left:775px"><span class="qmark">“</span>Lorem ipsum dolor sit amet, consect<br>er adipiscing elit, sed diam nonummy<br>nibh euismod tincidunt ut laoreet do<br>magna aliquam erat volu. Wisi enim<br>minim veniam.<span class="qclose">”</span></div>
    <div class="avatar" style="left:987px;top:299px" role="img" aria-label="Portrait of customer Owen Castellane"></div>
    <div class="tname" style="left:778px">Owen Castellane</div>
  </section>

  <section class="about">
    <h2>ABOUT US</h2>
    <p>Lorem ipsum dolor sit amet, consectetur adipiscing elit, sed do eiusmod tempor incididunt ut labore et dolore magna aliqua. Ut enim ad minim veniam, quis nostrud exercitation ullamco laboris nisi ut aliquip ex ea commodo consequat. Duis aute irure dolor in reprehender it in voluptate velit esse cillum dolore eu fugiat nulla pariatur. Excepteur sint occaecat cupi datat non proident, sunt in culpa qui officia deserunt mollit anim id est laborum.</p>
    <div class="abs btn-solid">LEARN MORE</div>
    <div class="abs about-ring"><div class="about-photo" role="img" aria-label="Photo of construction engineers in hard hats overlooking an excavator and city skyline"></div></div>
  </section>

  <footer class="site-footer">
    <div class="abs footer-logo">Quorvantelline.com</div>

    <div class="fcol" style="left:77px;width:135px">
      <h4>QUICK LINKS</h4>
      <ul><li>Home</li><li>Products</li><li>Shop</li><li>Testimonials</li><li>About</li><li>Contact</li></ul>
    </div>
    <div class="fcol" style="left:241px;width:130px">
      <h4>INFORMATION</h4>
      <ul><li>FAQs</li><li>Terms &amp; Conditions</li><li>Shipping</li><li>Return Policy</li></ul>
    </div>
    <div class="fcol" style="left:424px;width:196px">
      <h4>CONTACT</h4>
      <div class="contact-row"><svg width="16" height="18" viewBox="0 0 24 28"><path d="M12 1a9 9 0 0 0-9 9c0 7 9 17 9 17s9-10 9-17a9 9 0 0 0-9-9z" fill="none" stroke="#fff" stroke-width="2.5"/><circle cx="12" cy="10" r="3" fill="#fff"/></svg><span>Quorvantelline.com<br>48 Harbor Reach Way<br>Tampa, FL 33602</span></div>
      <div class="contact-row"><svg width="16" height="16" viewBox="0 0 24 24"><circle cx="12" cy="12" r="10.5" fill="none" stroke="#fff" stroke-width="2"/><path fill="#fff" d="M8.5 10.5a8 8 0 0 0 5 5l1.4-1.4 2.6 1.2-.6 2.2c-4.6-.3-9.1-4.8-9.4-9.4l2.2-.6 1.2 2.6z"/></svg><span>1800.555.0142</span></div>
      <div class="contact-row"><svg width="16" height="16" viewBox="0 0 24 24"><circle cx="12" cy="12" r="10.5" fill="none" stroke="#fff" stroke-width="2"/><rect x="6.5" y="8" width="11" height="8" fill="#fff"/></svg><span>info@quorvantelline.com</span></div>
    </div>
    <div class="fcol" style="left:686px;width:120px">
      <h4>FOLLOW US</h4>
      <div class="social"><i></i>Pagebook</div>
      <div class="social"><i></i>Picstream</div>
    </div>
    <div class="fcol" style="left:841px;width:257px">
      <h4>NEWSLETTER</h4>
      <div class="newsletter"><div class="field">Enter Email Address</div><div class="go">SIGN UP</div></div>
    </div>
  </footer>

  <div class="copyright">COPYRIGHT © 2018 QUORVANTELLINE.COM. ALL RIGHTS RESERVED.</div>
</div>
</body>
</html>
```